Newsletter Teddos Track Weeks

Hello i need some Newsletter to promote my company and the new events that we make.
we are organist motorbike events in different circuits in europe

please wrote me when you need some other format from the logo

I need a Template that include the text blocks. in the moment i don’t have finish the text.

we need the newsletter to send in sozialmedia, e-mail and homepage.
its always for online we don’t print and send newsletter.

i will send the newsletters with the program direct mail

Target Market(s)

us target market are all motorbike stores and all motorbike riders.

Industry/Entity Type

Events

Requirements
Must have
• i don’t know :)
have to be us logo and see very cool and crazy..
My Homepage maybe can help
www.teddos-track-weeks.ch
Nice to have
• a link to my contact e-mail and web address

```html
<!DOCTYPE html>
<html lang="en">
<head>
<meta charset="utf-8">
<title>Teddos Track Weeks Newsletter</title>
<link rel="stylesheet" href="https://fonts.googleapis.com/css2?family=Saira:ital,wght@0,500;1,400;1,800&family=Didact+Gothic&family=Montserrat:wght@500&display=swap">
<style>
  :root {
    --red: #e4262c;
    --red-dark: #a8141a;
    --grey-light: #e6e6e6;
    --grey-mid: #c6c6c6;
    --ink: #2b2b2b;
    --white: #ffffff;
    --page: #ffffff;
  }
  * { margin: 0; padding: 0; box-sizing: border-box; }
  html, body { width: 954px; height: 1200px; overflow: hidden; background: var(--page); }
  .newsletter {
    position: relative;
    width: 954px;
    height: 1200px;
    overflow: hidden;
    background: radial-gradient(ellipse at 50% 55%, var(--grey-light), var(--grey-mid));
    font-family: "Didact Gothic", sans-serif;
    color: var(--ink);
  }
  .backdrop { position: absolute; inset: 0; }
  .masthead-title {
    position: absolute;
    left: 40px; top: 52px;
    font-family: "Saira", sans-serif;
    font-style: italic;
    font-weight: 800;
    font-size: 44px;
    line-height: 52px;
    letter-spacing: 6px;
    color: var(--white);
    text-transform: uppercase;
  }
  .brand {
    position: absolute;
    left: 596px; top: 369px;
    width: 314px;
    text-align: center;
  }
  .brand-name {
    display: flex; align-items: center; justify-content: center; gap: 8px;
    font-family: "Montserrat", sans-serif;
    font-weight: 500;
    font-size: 20px;
    line-height: 26px;
    color: #222;
    text-transform: uppercase;
  }
  .brand-mark { width: 12px; height: 12px; background: var(--red); }
  .brand-tagline {
    font-family: "Montserrat", sans-serif;
    font-size: 10px;
    letter-spacing: 4px;
    color: #333;
    text-transform: uppercase;
    margin-top: 2px;
  }
  .headline {
    position: absolute;
    left: 508px; top: 441px;
    width: 410px;
    font-family: "Saira", sans-serif;
    font-style: italic;
    font-weight: 400;
    font-size: 29px;
    line-height: 38px;
    color: var(--white);
  }
  .story { position: absolute; width: 403px; }
  .story h2 {
    font-family: "Saira", sans-serif;
    font-style: italic;
    font-weight: 400;
    font-size: 26px;
    line-height: 30px;
    color: var(--red);
    margin-bottom: 12px;
  }
  .story p {
    font-size: 15px;
    line-height: 18.2px;
    text-align: justify;
    margin-bottom: 18px;
  }
  .story-feature { left: 53px; top: 540px; }
  .story-other-right { left: 507px; top: 540px; }
  .story-other-left { left: 53px; top: 928px; }
  .contact-bar {
    position: absolute;
    left: 0; right: 0; top: 1160px;
    height: 28px;
  }
  .contact-item {
    position: absolute;
    top: 0;
    display: flex; align-items: center; gap: 5px;
    font-family: "Saira", sans-serif;
    font-style: italic;
    font-size: 19px;
    color: var(--white);
    text-decoration: none;
    white-space: nowrap;
  }
  .contact-email { left: 46px; }
  .contact-web { left: 388px; }
  .contact-phone { left: 730px; }
  .contact-item svg { width: 16px; height: 16px; }
</style>
</head>
<body>
<main class="newsletter">
  <svg class="backdrop" width="954" height="1200" viewBox="0 0 954 1200">
    <defs>
      <linearGradient id="trackPhoto" x1="0" y1="0" x2="1" y2="1">
        <stop offset="0" stop-color="#8a9560"/>
        <stop offset="0.35" stop-color="#6d6f6c"/>
        <stop offset="1" stop-color="#5b5d60"/>
      </linearGradient>
      <linearGradient id="riderPhoto" x1="0" y1="0" x2="1" y2="0">
        <stop offset="0" stop-color="#3a3a3c"/>
        <stop offset="1" stop-color="#1c1c1e"/>
      </linearGradient>
      <linearGradient id="flagArea" x1="0" y1="0" x2="1" y2="1">
        <stop offset="0" stop-color="#f0f0f0"/>
        <stop offset="1" stop-color="#555"/>
      </linearGradient>
      <linearGradient id="footerRed" x1="0" y1="0" x2="0" y2="1">
        <stop offset="0" stop-color="#e4262c"/>
        <stop offset="1" stop-color="#a8141a"/>
      </linearGradient>
    </defs>

    <path role="img" aria-label="Photo of motorbike racers leaning through a curve on a race track"
          fill="url(#trackPhoto)"
          d="M0 0 H954 V300 C760 325 560 400 420 440 C300 470 150 478 0 468 Z"/>
    <path fill="var(--red)"
          d="M0 468 C150 478 300 470 420 440 C560 400 760 325 954 300 V328 C780 345 600 410 450 465 C300 505 130 508 0 492 Z"/>
    <path fill="none" stroke="var(--red)" stroke-width="2"
          d="M460 478 C600 430 760 372 954 350"/>

    <rect role="img" aria-label="Photo of a rider on a black sport motorbike"
          x="503" y="917" width="340" height="231" rx="60" fill="url(#riderPhoto)" opacity="0.9"/>
    <rect role="img" aria-label="Waving chequered race flag"
          x="843" y="921" width="111" height="200" fill="url(#flagArea)"/>

    <path fill="url(#footerRed)"
          d="M0 1106 C250 1145 600 1150 954 1108 V1200 H0 Z"/>

    <path fill="var(--red)" d="M502 434 H926 L908 524 H483 Z"/>
  </svg>

  <h1 class="masthead-title">Newsletter</h1>

  <div class="brand">
    <div class="brand-name"><span class="brand-mark"></span>Teddos Track Weeks</div>
    <div class="brand-tagline">Ride fast and ride safe</div>
  </div>

  <p class="headline">Lorem ipsum dolor sit amet,<br>consectetuer adipiscing elit</p>

  <section class="story story-feature">
    <h2>Feature story</h2>
    <p>Lorem ipsum dolor sit amet, consectetuer adipiscing elit, sed diam nonummy nibh euismod tincidunt ut laoreet dolore magna aliquam erat volutpat. Ut wisi enim ad minim veniam, quis nostrud exerci tation ullamcorper suscipit lobortis nisl ut aliquip ex ea commodo consequat. Duis autem vel eum iriure dolor in hendrerit in vulputate velit esse molestie consequat, vel illum dolore eu feugiat nulla facilisis at vero eros et accumsan et iusto odio dignissim qui blandit praesent luptatum zzril delenit augue duis dolore te feugait nulla facilisi.</p>
    <p>Lorem ipsum dolor sit amet, consectetuer adipiscing elit, sed diam nonummy nibh euismod tincidunt ut laoreet dolore magna aliquam erat volutpat. Ut wisi enim ad minim veniam, quis nostrud exerci tation ullamcorper suscipit lobortis nisl ut aliquip ex ea commodo consequat.</p>
  </section>

  <section class="story story-other-right">
    <h2>Other story1</h2>
    <p>Lorem ipsum dolor sit amet, consectetuer adipiscing elit, sed diam nonummy nibh euismod tincidunt ut laoreet dolore magna aliquam erat volutpat. Ut wisi enim ad minim veniam, quis nostrud exerci tation ullamcorper suscipit lobortis nisl ut aliquip ex ea commodo consequat. Duis autem vel eum iriure dolor in hendrerit in vulputate velit esse molestie consequat, vel illum dolore eu feugiat nulla facilisis at vero eros et accumsan et iusto odio dignissim qui blandit praesent luptatum zzril delenit augue duis dolore te feugait nulla facilisi.</p>
    <p>Lorem ipsum dolor sit amet, consectetuer adipiscing elit, sed diam nonummy nibh euismod tincidunt ut laoreet dolore magna aliquam erat volutpat. Ut wisi enim ad minim veniam, quis nostrud exerci tation ullamcorper suscipit lobortis nisl ut aliquip ex ea commodo consequat.</p>
  </section>

  <section class="story story-other-left">
    <h2>Other story1</h2>
    <p>Lorem ipsum dolor sit amet, consectetuer adipiscing elit, sed diam nonummy nibh euismod tincidunt ut laoreet dolore magna aliquam erat volutpat. Ut wisi enim ad minim veniam, quis nostrud exerci tation ullamcorper suscipit lobortis nisl ut aliquip ex ea commodo consequat. Duis autem vel eum iriure dolor in hendrerit in vulputate velit esse molestie consequat.</p>
  </section>

  <footer class="contact-bar">
    <a class="contact-item contact-email" href="mailto:info@teddos-track-weeks.ch">
      <svg viewBox="0 0 16 16"><rect x="1" y="3" width="14" height="10" fill="none" stroke="#fff" stroke-width="1.5"/><path d="M1 3 L8 9 L15 3" fill="none" stroke="#fff" stroke-width="1.5"/></svg>
      info@teddos-track-weeks.ch
    </a>
    <a class="contact-item contact-web" href="https://www.teddos-track-weeks.ch">
      <svg viewBox="0 0 16 16"><circle cx="8" cy="8" r="6.5" fill="none" stroke="#fff" stroke-width="1.4"/><ellipse cx="8" cy="8" rx="2.8" ry="6.5" fill="none" stroke="#fff" stroke-width="1.2"/><path d="M1.5 8 H14.5 M3 4.5 H13 M3 11.5 H13" stroke="#fff" stroke-width="1.1"/></svg>
      www.teddos-track-weeks.ch
    </a>
    <a class="contact-item contact-phone" href="tel:+41765551234">
      <svg viewBox="0 0 16 16"><circle cx="8" cy="8" r="7" fill="none" stroke="#fff" stroke-width="1.3"/><path d="M5.5 4 L7 5.8 L6.2 7 C6.8 8.3 7.7 9.2 9 9.8 L10.2 9 L12 10.5 L11 12 C8 11.8 4.2 8 4 5 Z" fill="#fff"/></svg>
      +41 (0)76 555 12 34
    </a>
  </footer>
</main>
</body>
</html>
```